Soap Company Looking To Design New Soap Scent Boxes

we are looking to create a soap box similar to pa grunwell. we would like the circle cut out on the top right corner of the box. we are looking for a design that will allow us to use different color base banners for different soap scents (like pa. grunwell). we want the soap name scents to be large and readable on the bottom banner (like pa.grunwell). we have included our brand figure (logo) and some previous older soap box designs that we were making before the brand figure. the box dims are attached.

```html
<!DOCTYPE html>
<html lang="en">
<head>
<meta charset="utf-8">
<title>Hollow Fern – Plumeria Soap Box</title>
<link rel="stylesheet" href="https://fonts.googleapis.com/css2?family=Fredoka:wght@600&family=Lato:wght@700&display=swap">
<style>
  :root {
    --page: #ffffff;
    --kraft: #d4b185;
    --banner-green: #358243;
    --ink-brown: #2f1b15;
    --cutout-grey: #8c8f93;
    --cutout-dark: #6e7175;
    --bubble: #ffffff;
    --text-light: #ffffff;
  }
  * { margin: 0; padding: 0; box-sizing: border-box; }
  html, body {
    width: 1200px; height: 867px; overflow: hidden;
    background: var(--page);
  }
  .canvas { position: relative; width: 1200px; height: 867px; }
  .box-front {
    position: absolute; left: 318px; top: 147px;
    width: 567px; height: 573px;
    background: var(--kraft);
  }
  .cutout {
    position: absolute; left: 455px; top: 22px;
    width: 90px; height: 90px; border-radius: 50%;
    background: radial-gradient(circle at 50% 45%, var(--cutout-grey) 60%, var(--cutout-dark) 100%);
  }
  .bubble { position: absolute; border-radius: 50%; background: var(--bubble); }
  .bubble--large  { left: 440px; top: 85px;  width: 46px; height: 46px; }
  .bubble--medium { left: 404px; top: 118px; width: 35px; height: 35px; }
  .bubble--small  { left: 372px; top: 130px; width: 22px; height: 22px; }
  .brand-name {
    position: absolute; left: 0; right: 0; top: 200px;
    text-align: center;
    font-family: "Fredoka", sans-serif; font-weight: 600;
    font-size: 62px; line-height: 1;
    color: var(--ink-brown);
  }
  .scent-banner {
    position: absolute; left: 0; top: 371px;
    width: 567px; height: 170px;
  }
  .scent-banner svg { position: absolute; inset: 0; }
  .scent-name, .scent-type, .net-weight {
    position: absolute; left: 0; right: 0; text-align: center;
    color: var(--text-light);
  }
  .scent-name {
    top: 22px;
    font-family: "Fredoka", sans-serif; font-weight: 600;
    font-size: 74px; line-height: 76px; letter-spacing: 2px;
  }
  .scent-type {
    top: 95px;
    font-family: "Fredoka", sans-serif; font-weight: 600;
    font-size: 22px; line-height: 24px; letter-spacing: 2.5px;
  }
  .net-weight {
    top: 129px;
    font-family: "Lato", sans-serif; font-weight: 700;
    font-size: 16px; line-height: 20px;
  }
</style>
</head>
<body>
<main class="canvas">
  <section class="box-front">
    <div class="cutout" aria-hidden="true"></div>
    <div class="bubble bubble--large" aria-hidden="true"></div>
    <div class="bubble bubble--medium" aria-hidden="true"></div>
    <div class="bubble bubble--small" aria-hidden="true"></div>

    <h1 class="brand-name">Hollow Fern</h1>

    <div class="scent-banner">
      <svg width="567" height="170" viewBox="0 0 567 170" aria-hidden="true">
        <defs>
          <pattern id="scallop-top" width="14" height="14" patternUnits="userSpaceOnUse">
            <circle cx="7" cy="8" r="7" fill="#358243"/>
          </pattern>
          <pattern id="scallop-bottom" width="14" height="14" patternUnits="userSpaceOnUse" y="156">
            <circle cx="7" cy="6" r="7" fill="#358243"/>
          </pattern>
        </defs>
        <rect x="0" y="0" width="567" height="14" fill="url(#scallop-top)"/>
        <rect x="0" y="8" width="567" height="154" fill="#358243"/>
        <rect x="0" y="156" width="567" height="14" fill="url(#scallop-bottom)"/>
      </svg>
      <h2 class="scent-name">PLUMERIA</h2>
      <p class="scent-type">COLD PRESSED ARTISAN SOAP</p>
      <p class="net-weight">Net Wt. 5oz (140g)</p>
    </div>
  </section>
</main>
</body>
</html>
```